bright meridian advisory needs a business card

i need a business card with a logo that will also be used on the website. The company name is "Bright Meridian Advisory"
The business is an advisory and training organisation that specialises in finding a companys 'natural sequence' to success but we will also provide mentoring and counselling to individuals that want to unlock their potential. The process is unique and not full of the normal corporate bullshit so the card should be 'different' and innovative in use of texture, colour, layout etc...I have no guiding principles for you but if you were the head of a new company lloking to make a great first impression what would your card look like? It should have enough of the corporate that the stiffs dont get scared but should be cool enough that the cool kids get it :-)

Target Market(s)

Companies and people looking to grow their staff capabilities. Specialising in IT but can transcend that to other lines of business.

Industry/Entity Type

It Company

Contact Information for Business Card

usuall placeholder stuff Name, Number etc

Requirements
Must have
• cool and innovative logo and use of space
Nice to have
• Background image, subtle use of the caffeine molecule
• A rollable business card similar to the attached image. Would be nice if either side of the card could be half of a DNA helix and by rolling 2 sides together they could connect at one or more points....Perhaps the strands between have a message?
Should not have
• boring usual business card look and feel

```html
<!DOCTYPE html>
<html lang="en">
<head>
<meta charset="utf-8">
<title>Bright Meridian Advisory – Business Card</title>
<link rel="stylesheet" href="https://fonts.googleapis.com/css2?family=Questrial&display=swap">
<style>
  :root {
    --brand-blue: #3b7dc6;
    --card-white: #ffffff;
    --ink-grey: #5d6670;
    --rule-grey: #b9bec4;
    --band-grey: #a7adb3;
    --stage: #eceeef;
  }
  * { margin: 0; padding: 0; box-sizing: border-box; }
  html, body {
    width: 1200px;
    height: 839px;
    overflow: hidden;
    background: var(--stage);
    font-family: "Questrial", "Century Gothic", sans-serif;
  }
  .canvas { position: relative; width: 1200px; height: 839px; }
  .card {
    position: absolute;
    top: 274px;
    width: 578px;
    height: 323px;
    overflow: hidden;
    box-shadow: 0 2px 6px rgba(0,0,0,0.18);
  }
  /* Front */
  .card-front { left: 21px; background: var(--brand-blue); }
  .front-helix {
    position: absolute;
    top: 0;
    right: 0;
    width: 340px;
    height: 240px;
    background: radial-gradient(ellipse at 70% 35%, rgba(220,238,255,0.7) 0%, rgba(160,205,245,0.4) 40%, rgba(59,125,198,0) 72%);
  }
  .front-brand {
    position: absolute;
    left: 50px;
    top: 212px;
    color: var(--card-white);
    font-size: 32px;
    line-height: 40px;
    white-space: nowrap;
  }
  .front-tagline {
    position: absolute;
    left: 52px;
    top: 272px;
    color: var(--card-white);
    font-size: 11.5px;
    letter-spacing: 1px;
    text-transform: uppercase;
    white-space: nowrap;
  }
  /* Back */
  .card-back { left: 606px; background: var(--card-white); }
  .back-helix {
    position: absolute;
    left: 0;
    top: 0;
    width: 300px;
    height: 190px;
    background: radial-gradient(ellipse at 55% 30%, rgba(200,212,225,0.55) 0%, rgba(225,232,240,0.35) 45%, rgba(255,255,255,0) 75%);
  }
  .back-brand {
    position: absolute;
    left: 318px;
    top: 50px;
    width: 230px;
    color: var(--brand-blue);
    font-size: 27px;
    line-height: 32px;
  }
  .holder-name {
    position: absolute;
    left: 30px;
    top: 176px;
    color: var(--brand-blue);
    font-size: 23px;
    letter-spacing: 0.5px;
  }
  .holder-role {
    position: absolute;
    left: 30px;
    top: 208px;
    color: var(--ink-grey);
    font-size: 11px;
    letter-spacing: 0.6px;
  }
  .divider {
    position: absolute;
    left: 30px;
    top: 238px;
    width: 522px;
    height: 1px;
    background: var(--rule-grey);
  }
  .address {
    position: absolute;
    left: 30px;
    top: 255px;
    color: var(--ink-grey);
    font-size: 10.5px;
  }
  .contact-row {
    position: absolute;
    left: 30px;
    top: 276px;
    display: flex;
    align-items: center;
    gap: 8px;
    color: var(--ink-grey);
    font-size: 10.5px;
    white-space: nowrap;
  }
  .contact-item { display: flex; align-items: center; gap: 5px; }
  .contact-item svg { width: 12px; height: 12px; }
  .sep { color: var(--rule-grey); }
  .base-band {
    position: absolute;
    left: 0;
    bottom: 0;
    width: 100%;
    height: 7px;
    display: flex;
  }
  .base-band .blue { width: 405px; background: var(--brand-blue); }
  .base-band .grey { flex: 1; background: var(--band-grey); }
</style>
</head>
<body>
<main class="canvas">
  <section class="card card-front">
    <div class="front-helix" role="img" aria-label="Translucent DNA double helix illustration"></div>
    <div class="front-brand">Bright Meridian Advisory</div>
    <div class="front-tagline">Guiding you toward a clearer path</div>
  </section>

  <section class="card card-back">
    <div class="back-helix" role="img" aria-label="Faint grey DNA double helix illustration"></div>
    <div class="back-brand">Bright Meridian Advisory</div>
    <div class="holder-name">ALEX CARTER</div>
    <div class="holder-role">MEMBER</div>
    <div class="divider"></div>
    <div class="address">P.O. Box 518, Fairview, VA 22031</div>
    <div class="contact-row">
      <span class="contact-item">
        <svg viewBox="0 0 12 12" aria-hidden="true"><path d="M1 4c0-1.5 2-2.5 5-2.5S11 2.5 11 4l-2 1-1-1.3H4L3 5 1 4zM2.5 6h7l1 4.5h-9z" fill="#3b7dc6"/></svg>
        555.014.2290
      </span>
      <span class="sep">|</span>
      <span class="contact-item">
        <svg viewBox="0 0 12 12" aria-hidden="true"><rect x="1" y="2.5" width="10" height="7" fill="none" stroke="#3b7dc6"/><path d="M1 2.5l5 4 5-4" fill="none" stroke="#3b7dc6"/></svg>
        alex@brightmeridian.example
      </span>
      <span class="sep">|</span>
      <span class="contact-item">
        <svg viewBox="0 0 12 12" aria-hidden="true"><circle cx="6" cy="6" r="5" fill="none" stroke="#3b7dc6"/><ellipse cx="6" cy="6" rx="2.2" ry="5" fill="none" stroke="#3b7dc6"/><path d="M1 6h10" stroke="#3b7dc6"/></svg>
        www.brightmeridian.example
      </span>
    </div>
    <div class="base-band"><span class="blue"></span><span class="grey"></span></div>
  </section>
</main>
</body>
</html>
```